Poster design for Non-Profit Harbor Pathways

Harbor Pathways is a not-for-profit providing disability services to improve the lives of the people we serve. We are holding an internal convention with staff focusing on improving what we already do well. The title of the event and ongoing effort will be ‘Ventus Aperta’, with a sub-title of ‘Focusing on our Strengths’.

Target Market(s)

Our employees

Industry/Entity Type

Non Profit

Font styles to use
Serif

Requirements
Must have
• • Be A0 size
• • Include the title ‘Ventus Aperta’
• • Include the sub-title ‘ Focusing on our Strengths’
• • Include the Harbor Pathways Logo
• • A colour scheme that ties in to our logo
Nice to have
• A bold, minimalist design with clear lettering. Refer to the files inspiration 1 and 2. Also I will upload a brochure we had designed recently. Please ignore our website for design features as it is outdated.
Should not have
• Too many photos.

```html
<!DOCTYPE html>
<html lang="en">
<head>
<meta charset="utf-8">
<title>Ventus Aperta — Focusing on our Strengths</title>
<link rel="stylesheet" href="https://fonts.googleapis.com/css2?family=Barlow+Condensed:ital,wght@1,600;1,800&display=swap">
<style>
  :root {
    --paper: #ffffff;
    --magenta: #d13bd6;
    --violet: #8a3fd8;
    --deep-violet: #5a2fb8;
    --lilac: #b98ae8;
    --white: #ffffff;
    --brand-purple: #4b2a7a;
  }
  html, body {
    margin: 0;
    padding: 0;
    overflow: hidden;
    background: var(--paper);
  }
  .poster {
    position: relative;
    width: 849px;
    height: 1200px;
    background: var(--paper);
    overflow: hidden;
    font-family: "Barlow Condensed", "Arial Narrow", sans-serif;
  }
  .hero-panel {
    position: absolute;
    left: 34px;
    top: 0;
    width: 781px;
    height: 957px;
    background:
      radial-gradient(circle at 80% 55%, rgba(255,220,255,0.35) 0, rgba(255,220,255,0) 35%),
      radial-gradient(circle at 15% 40%, rgba(255,200,255,0.25) 0, rgba(255,200,255,0) 30%),
      linear-gradient(160deg, var(--magenta) 0%, var(--violet) 55%, var(--lilac) 100%);
  }
  .event-title {
    position: absolute;
    top: 40px;
    left: 0;
    width: 100%;
    margin: 0;
    text-align: center;
    font-weight: 800;
    font-style: italic;
    font-size: 104px;
    line-height: 98px;
    letter-spacing: 2px;
    text-transform: uppercase;
    color: transparent;
    -webkit-text-stroke: 4px var(--white);
  }
  .rule {
    position: absolute;
    left: 34px;
    width: 713px;
    height: 3px;
    background: var(--white);
  }
  .rule--top { top: 250px; }
  .rule--bottom { top: 650px; }
  .event-subtitle {
    position: absolute;
    top: 272px;
    left: 0;
    width: 100%;
    margin: 0;
    text-align: center;
    font-weight: 600;
    font-style: italic;
    font-size: 142px;
    line-height: 120px;
    letter-spacing: 3px;
    text-transform: uppercase;
    color: var(--white);
  }
  .brand {
    position: absolute;
    top: 1040px;
    left: 0;
    width: 100%;
    display: flex;
    justify-content: center;
    align-items: center;
    gap: 18px;
  }
  .brand-dot {
    width: 44px;
    height: 44px;
    border-radius: 50%;
    background: var(--brand-purple);
  }
  .brand-name {
    font-weight: 800;
    font-style: italic;
    font-size: 54px;
    letter-spacing: 1px;
    text-transform: uppercase;
    color: var(--brand-purple);
  }
</style>
</head>
<body>
  <main class="poster">
    <section class="hero-panel">
      <h1 class="event-title">Ventus<br>Aperta</h1>
      <div class="rule rule--top"></div>
      <h2 class="event-subtitle">Focusing<br>on our<br>strengths</h2>
      <div class="rule rule--bottom"></div>
    </section>
    <footer class="brand">
      <span class="brand-dot"></span>
      <span class="brand-name">Harbor Pathways</span>
    </footer>
  </main>
</body>
</html>
```